LUSTRIA INC. is a new Fashion Stylist, Design Merchandiser, and consultant in the fashion industry

We need a logo design for a new Calgary, Alberta based company that is in the business of making over your image, wardrobe and style for both business and personal purposes.

Target Market(s)

Professional female and male business people looking for a new style or complete fashion makeover including clothes closet merchandising and makeover.

Contact Information for Business Card

Number of Pages Required

1 page

Font styles to use
Script

Colors
fac994
fbe7d2
fee3d4

Requirements
Must have
• Fashion Industry theme that is very elegant and colorful using gold/bronze/silver color themes.
Nice to have
• Incorporate the company name with the creative font to come up with the appropriate "logo"

```html
<!DOCTYPE html>
<html lang="en">
<head>
<meta charset="utf-8">
<title>Margot Ellery — Business Card</title>
<link rel="stylesheet" href="https://fonts.googleapis.com/css2?family=Pinyon+Script&family=Marcellus+SC&display=swap">
<style>
  :root {
    --ink: #8f8c8c;
    --peach: #f6b9a4;
    --blush: #fee3d4;
    --cream: #fbe7d2;
    --gold: #fac994;
    --lilac: #f1d6e6;
    --paper: #fffaf6;
  }
  html, body {
    margin: 0;
    padding: 0;
    overflow: hidden;
    background: var(--paper);
  }
  .card-spread {
    position: relative;
    width: 1200px;
    height: 343px;
    overflow: hidden;
    display: flex;
  }
  .card-side {
    position: relative;
    width: 600px;
    height: 343px;
    overflow: hidden;
  }
  .wash {
    position: absolute;
    inset: 0;
  }
  .wash--front {
    background:
      radial-gradient(ellipse 260px 120px at 110px 90px, rgba(246,185,164,.75), transparent 70%),
      radial-gradient(ellipse 220px 110px at 420px 230px, rgba(246,185,164,.7), transparent 70%),
      radial-gradient(ellipse 200px 160px at 520px 70px, rgba(250,201,148,.55), transparent 70%),
      radial-gradient(ellipse 180px 120px at 60px 280px, rgba(241,214,230,.8), transparent 70%),
      radial-gradient(ellipse 240px 100px at 300px 320px, rgba(246,185,164,.5), transparent 70%),
      linear-gradient(120deg, var(--blush), var(--paper) 45%, var(--cream));
  }
  .wash--back {
    background:
      linear-gradient(100deg, transparent 8%, rgba(246,185,164,.55) 14%, rgba(246,185,164,.45) 24%, transparent 32%),
      radial-gradient(ellipse 220px 160px at 520px 90px, rgba(246,185,164,.65), transparent 70%),
      radial-gradient(ellipse 200px 140px at 380px 260px, rgba(246,185,164,.45), transparent 70%),
      radial-gradient(ellipse 220px 150px at 200px 200px, rgba(250,201,148,.5), transparent 70%),
      radial-gradient(ellipse 160px 120px at 40px 80px, rgba(241,214,230,.8), transparent 70%),
      linear-gradient(90deg, var(--lilac), var(--cream) 40%, var(--blush));
  }
  .brand-mark {
    position: absolute;
    left: 120px;
    top: 120px;
    width: 420px;
    height: 110px;
    display: flex;
    align-items: center;
    gap: 22px;
  }
  .brand-mark__circle {
    flex: none;
    width: 86px;
    height: 86px;
    border: 2px solid var(--ink);
    border-radius: 50%;
    box-sizing: border-box;
  }
  .brand-mark__name {
    margin: 0;
    font-family: "Pinyon Script", cursive;
    font-weight: 400;
    font-size: 54px;
    line-height: 1;
    color: var(--ink);
    white-space: nowrap;
  }
  .services {
    position: absolute;
    top: 24px;
    left: 0;
    right: 0;
    margin: 0;
    padding: 0;
    list-style: none;
    font-family: "Marcellus SC", serif;
    font-size: 18px;
    color: var(--ink);
  }
  .services li { position: absolute; white-space: nowrap; }
  .services .service--stylist { left: 28px; }
  .services .service--merchandiser { left: 203px; }
  .services .service--consultant { left: 462px; }
  .holder-name {
    position: absolute;
    left: 0;
    right: 0;
    top: 128px;
    margin: 0;
    font-family: "Pinyon Script", cursive;
    font-weight: 400;
    font-size: 56px;
    line-height: 46px;
    color: var(--ink);
    text-align: center;
  }
  .holder-name span { display: block; }
  .holder-name .first { margin-left: 30px; }
  .holder-name .last { margin-right: 10px; }
  .phone {
    position: absolute;
    left: 300px;
    top: 308px;
    transform: translate(-50%, -50%);
    margin: 0;
    font-family: "Marcellus SC", serif;
    font-size: 17px;
    letter-spacing: .5px;
    color: var(--ink);
  }
</style>
</head>
<body>
  <main class="card-spread">
    <section class="card-side card-side--front">
      <div class="wash wash--front" role="img" aria-label="Soft peach, blush and gold watercolour wash"></div>
      <div class="brand-mark">
        <span class="brand-mark__circle" aria-hidden="true"></span>
        <h1 class="brand-mark__name">Margot Ellery</h1>
      </div>
    </section>
    <section class="card-side card-side--back">
      <div class="wash wash--back" role="img" aria-label="Soft peach, lilac and gold watercolour brush strokes"></div>
      <ul class="services">
        <li class="service--stylist">Fashion Stylist</li>
        <li class="service--merchandiser">Design Merchandiser</li>
        <li class="service--consultant">Consultant</li>
      </ul>
      <h2 class="holder-name"><span class="first">Margot</span><span class="last">Ellery</span></h2>
      <p class="phone">403.555.0148</p>
    </section>
  </main>
</body>
</html>
```